Puzzle (both moving graphic) and a printable piece.

I am looking for a "High Definition" graphic of a puzzle. Much like the one on our website where you first do to it -
www.thepellvanecompany.com

See the attachment for a blank puzzle that is what I'm talking about. I have also included a picture that I want the wording to say.

We will be using the puzzle as a marketing campaign and I would like to put it on our website and use it in print.

The puzzle picture, will be about retirement and all of the puzzle pieces involved.

a) It will have 12 pieces - Each piece will have something written on it - (see attachment)
b) there will be one piece missing.
So I want a moving graphic with the puzzle coming together - I also want a high resolution for printing purposes.

Thanks, Dwight

I have received 2 submissions so far, one of the submissions is blurry and not clear. I added the pictures of the puzzle for the designer’s reference – you don’t have to use the same puzzle – you can create your own.

Any submissions needs to be crystal clear and high definition

 

Also try to have the wording on each puzzle piece so centered, so it is not near the edges of the puzzle pieces.

 

Update to my first submissions: The wording on the 12 puzzle pieces are as follows. (The pieces can be in any order that works for you)

 

#1 piece) Required Minimum Distribution

#2 piece) Social Security

#3 piece) Pensions

#4 piece) Medicare and Drug Plan

#5 piece) ROTH

#6 piece) Long Term Care

#7 piece) Guaranteed Lifetime Income

#8 piece) Wealth Transfer

#9 piece) Taxes & Inflation

#10 piece) IRA

#11 piece) 401k Rollover

In the moving graphic for the website (it should be 2 rows of 6 columns) – I would like piece # 12 to come in to the puzzle last, to complete the puzzle.

 

#12 piece) RETIREMENT Sleep Well at Night

 

Then I would like to have words come above the puzzle, which says “We are the final piece that helps you complete your retirement puzzle

 

For the high definition printable graphic, (it should be 3 rows of 4 columns)

 

I would like to have the #12 piece) RETIREMENT Sleep Well at Night – to be lying beside the puzzle.  

 

So this puzzle will have one piece missing, and #12 will be lying on the side of the puzzle. And above the puzzle – I would like it to say “We are the final piece that helps you complete your retirement puzzle

Reason: I have been out of town and unavailable. I'm going out town again tomorrow. So I need additional time.

Hello - I appologize for being out of touch for a while - I had to go out of toiwn for business. I have just made this project guarenteed. I will be in touch with some of you to make cahnges and update to your offerings. Keep the great ideas coming.

Thank You Dwight

Thanks to all of the designers that took part in this project. I am very very happy with the results. I will start awarding the payments very soon. This is my first time using ArtHive, so I have to figure out how to do it. So bear with me, I'll get it done.

Thanks Again !!!   GREAT JOB GUYS !

Dwight Pellvane

Baby Boomers and Retirees

Marketing

```html
<!DOCTYPE html>
<html lang="en">
<head>
<meta charset="utf-8">
<title>Retirement Puzzle – Pellvane Retirement Strategies</title>
<link rel="stylesheet" href="https://fonts.googleapis.com/css2?family=Cabin:wght@500&family=Tinos&display=swap">
<style>
  :root {
    --wood-light: #a8692e;
    --wood-mid: #8a5322;
    --wood-dark: #4e2c10;
    --headline: #e6e6e2;
    --ink: #161616;
    --rmd: #10893c;
    --social: #989a9c;
    --pensions: #a6a24c;
    --medicare: #977cae;
    --roth: #363c8c;
    --ltc: #3a9b95;
    --income: #2e8a40;
    --wealth: #b0a628;
    --taxes: #871c22;
    --ira: #891a88;
    --rollover: #94a46a;
    --final: #3c9dc2;
    --brand-mark: #2b5a8e;
  }
  html, body {
    margin: 0;
    padding: 0;
    overflow: hidden;
    background: var(--wood-dark);
  }
  .canvas {
    position: relative;
    width: 1200px;
    height: 675px;
    overflow: hidden;
  }
  .tabletop {
    position: absolute;
    inset: 0;
    background:
      radial-gradient(ellipse at 60% 45%, rgba(0,0,0,0) 35%, rgba(0,0,0,0.55) 100%),
      linear-gradient(90deg, var(--wood-mid), var(--wood-light) 45%, var(--wood-mid) 75%, var(--wood-light));
  }
  .headline {
    position: absolute;
    left: 0;
    top: 10px;
    width: 810px;
    margin: 0;
    text-align: center;
    font-family: "Cabin", sans-serif;
    font-weight: 500;
    font-size: 35px;
    line-height: 42px;
    color: var(--headline);
    text-shadow: 2px 3px 4px rgba(0,0,0,0.6);
  }
  .puzzle {
    position: absolute;
    left: 0;
    top: 0;
    width: 1200px;
    height: 675px;
  }
  .piece-shapes {
    filter: drop-shadow(2px 3px 3px rgba(0,0,0,0.45));
  }
  .piece-label {
    font-family: "Tinos", serif;
    fill: var(--ink);
    text-anchor: middle;
  }
  .brand {
    position: absolute;
    left: 805px;
    top: 110px;
    display: flex;
    align-items: center;
    gap: 14px;
  }
  .brand-square {
    width: 56px;
    height: 56px;
    background: var(--brand-mark);
  }
  .brand-name {
    font-family: "Cabin", sans-serif;
    font-weight: 500;
    font-size: 26px;
    line-height: 30px;
    color: var(--headline);
  }
</style>
</head>
<body>
<div class="canvas">
  <div class="tabletop" role="img" aria-label="Wooden tabletop surface in warm brown tones"></div>

  <h1 class="headline">We are the final piece that helps you<br>complete your retirement puzzle</h1>

  <svg class="puzzle" viewBox="0 0 1200 675" aria-label="Retirement puzzle with one piece missing">
    <g class="piece-shapes">
      <!-- piece bodies -->
      <rect x="52" y="97" width="178" height="173" fill="var(--rmd)"/>
      <rect x="230" y="97" width="188" height="173" fill="var(--social)"/>
      <rect x="418" y="97" width="190" height="173" fill="var(--pensions)"/>
      <rect x="608" y="97" width="155" height="173" fill="var(--medicare)"/>
      <rect x="52" y="270" width="178" height="195" fill="var(--roth)"/>
      <rect x="230" y="270" width="188" height="195" fill="var(--ltc)"/>
      <rect x="418" y="270" width="190" height="195" fill="var(--income)"/>
      <rect x="608" y="270" width="155" height="195" fill="var(--wealth)"/>
      <rect x="52" y="465" width="178" height="180" fill="var(--taxes)"/>
      <rect x="230" y="465" width="188" height="180" fill="var(--ira)"/>
      <rect x="418" y="465" width="190" height="180" fill="var(--rollover)"/>

      <!-- connecting knobs -->
      <circle cx="207" cy="172" r="27" fill="var(--social)"/>
      <circle cx="130" cy="292" r="27" fill="var(--rmd)"/>
      <circle cx="395" cy="175" r="27" fill="var(--pensions)"/>
      <circle cx="300" cy="250" r="27" fill="var(--ltc)"/>
      <circle cx="515" cy="292" r="27" fill="var(--pensions)"/>
      <circle cx="585" cy="178" r="27" fill="var(--medicare)"/>
      <circle cx="680" cy="252" r="27" fill="var(--wealth)"/>
      <circle cx="207" cy="372" r="27" fill="var(--ltc)"/>
      <circle cx="135" cy="445" r="27" fill="var(--taxes)"/>
      <circle cx="441" cy="362" r="27" fill="var(--ltc)"/>
      <circle cx="318" cy="445" r="27" fill="var(--ira)"/>
      <circle cx="631" cy="365" r="27" fill="var(--income)"/>
      <circle cx="510" cy="445" r="27" fill="var(--rollover)"/>
      <circle cx="207" cy="565" r="27" fill="var(--ira)"/>
      <circle cx="441" cy="565" r="27" fill="var(--ira)"/>

      <!-- sockets left open by the missing piece -->
      <circle cx="588" cy="565" r="27" fill="var(--wood-mid)"/>
      <circle cx="710" cy="452" r="27" fill="var(--wood-mid)"/>
    </g>

    <!-- labels -->
    <g class="piece-labels">
      <text class="piece-label" font-size="21"><tspan x="116" y="135">Required</tspan><tspan x="112" y="192">Minimum</tspan><tspan x="124" y="250">Distribution</tspan></text>
      <text class="piece-label" font-size="38"><tspan x="312" y="155">Social</tspan><tspan x="312" y="227">Security</tspan></text>
      <text class="piece-label" font-size="40" x="510" y="150">Pensions</text>
      <text class="piece-label" font-size="34"><tspan x="685" y="135">Medicare</tspan><tspan x="685" y="180">and Drug</tspan><tspan x="685" y="224">Plan</tspan></text>
      <text class="piece-label" font-size="37" x="100" y="385">ROTH</text>
      <text class="piece-label" font-size="36"><tspan x="320" y="348">Long Term</tspan><tspan x="320" y="392">Care</tspan></text>
      <text class="piece-label" font-size="21"><tspan x="540" y="358">Guaranteed</tspan><tspan x="537" y="387">Lifetime</tspan><tspan x="540" y="416">Income</tspan></text>
      <text class="piece-label" font-size="23"><tspan x="710" y="344">Wealth</tspan><tspan x="712" y="376">Transfer</tspan></text>
      <text class="piece-label" font-size="40"><tspan x="140" y="520">Taxes</tspan><tspan x="140" y="573">&amp;</tspan><tspan x="140" y="626">Inflation</tspan></text>
      <text class="piece-label" font-size="68" x="325" y="583">IRA</text>
      <text class="piece-label" font-size="38"><tspan x="506" y="545">401k</tspan><tspan x="512" y="625">Rollover</tspan></text>
    </g>

    <!-- final piece lying beside the puzzle -->
    <g class="final-piece" transform="translate(788 548) rotate(35)">
      <g class="piece-shapes">
        <rect x="-82" y="-84" width="164" height="168" fill="var(--final)"/>
        <circle cx="30" cy="-106" r="27" fill="var(--final)"/>
        <circle cx="-104" cy="0" r="27" fill="var(--final)"/>
      </g>
      <text class="piece-label" font-size="20"><tspan x="0" y="-20">RETIREMENT</tspan><tspan x="0" y="4">Sleep Well at</tspan><tspan x="0" y="28">Night</tspan></text>
    </g>
  </svg>

  <div class="brand">
    <div class="brand-square"></div>
    <div class="brand-name">Pellvane<br>Retirement Strategies</div>
  </div>
</div>
</body>
</html>
```